I work in creative/artistic projects across different mediums.
It needs to communicate creativity, style, sexy, uniqueness, individuality and sophistication.
It should not look corporate.
Colours I like are black silver gold deep purple, chocolate, orchid.
It doesn't have to make use of all these colours.
I do not like bright primary colors.
Updates

Project Deadline Extended
Reason: Still in the communication process and to allow the person enough time to finish the design. Though i should know in the next day or two. Thank you.

Target Market(s)

creatives and companies wanting to inject creativity into thier business.

Industry/Entity Type

Work

Contact Information for Business Card

Marcus Tellwick
0418592036
marcus@marcustellwick.com

quietgoldenhour.com.au

Requirements
Should not have
• Anything corporate OR OLD FASHIONED

```html
<!DOCTYPE html>
<html lang="en">
<head>
<meta charset="utf-8">
<title>Marcus Tellwick — Business Card</title>
<link rel="stylesheet" href="https://fonts.googleapis.com/css2?family=Roboto+Condensed:wght@700&family=Questrial&display=swap">
<style>
  :root {
    --backdrop: #9c9c9c;
    --card-top: #3b3939;
    --card-bottom: #2a2828;
    --silver: #c9c9c9;
    --silver-soft: #a9a9a9;
    --silver-dim: #6e6c6c;
    --band-glow: #5a5858;
  }
  * { margin: 0; padding: 0; box-sizing: border-box; }
  html, body {
    width: 1200px;
    height: 840px;
    overflow: hidden;
    background: var(--backdrop);
  }
  .canvas {
    position: relative;
    width: 1200px;
    height: 840px;
    display: flex;
    align-items: center;
    justify-content: center;
  }
  .business-card {
    position: relative;
    width: 960px;
    height: 548px;
    background: linear-gradient(180deg, var(--card-top) 0%, var(--card-bottom) 100%);
    overflow: hidden;
  }
  .accent-band {
    position: absolute;
    left: 0;
    top: 150px;
    width: 100%;
    height: 4px;
    background: linear-gradient(90deg, transparent 0%, var(--band-glow) 15%, var(--silver-dim) 60%, var(--band-glow) 90%, transparent 100%);
    box-shadow: 0 0 14px 3px rgba(110, 108, 108, 0.35);
  }
  .holder-name {
    position: absolute;
    right: 74px;
    top: 186px;
    font-family: "Roboto Condensed", "Arial Narrow", sans-serif;
    font-weight: 700;
    font-size: 84px;
    line-height: 1;
    letter-spacing: 0.5px;
    color: var(--silver-soft);
    background: linear-gradient(180deg, #d6d6d6 0%, #a4a4a4 100%);
    -webkit-background-clip: text;
    background-clip: text;
    -webkit-text-fill-color: transparent;
  }
  .name-rule {
    position: absolute;
    left: 0;
    top: 282px;
    width: 890px;
    height: 3px;
    background: linear-gradient(90deg, transparent 0%, var(--silver-dim) 20%, var(--silver) 75%, var(--silver-soft) 100%);
  }
  .contact-line {
    position: absolute;
    left: 28px;
    top: 342px;
    display: flex;
    align-items: center;
    gap: 30px;
    font-family: "Questrial", "Century Gothic", sans-serif;
    font-size: 20px;
    color: var(--silver-soft);
    letter-spacing: 0.3px;
  }
  .contact-item {
    display: flex;
    align-items: center;
    gap: 9px;
  }
  .contact-icon {
    width: 18px;
    height: 18px;
    flex: none;
  }
</style>
</head>
<body>
  <main class="canvas">
    <section class="business-card" aria-label="Business card of Marcus Tellwick">
      <div class="accent-band"></div>
      <h1 class="holder-name">Marcus Tellwick</h1>
      <div class="name-rule"></div>
      <ul class="contact-line">
        <li class="contact-item">
          <svg class="contact-icon" viewBox="0 0 18 18" aria-hidden="true">
            <circle cx="9" cy="9" r="7.5" fill="none" stroke="#a9a9a9" stroke-width="1.4"/>
            <circle cx="9" cy="9" r="2.6" fill="none" stroke="#a9a9a9" stroke-width="1.4"/>
            <path d="M11.6 6.5v3.6c0 1.3 2.2 1.3 2.2-0.6" fill="none" stroke="#a9a9a9" stroke-width="1.4"/>
          </svg>
          <span>marcus@marcustellwick.com</span>
        </li>
        <li class="contact-item">
          <svg class="contact-icon" viewBox="0 0 18 18" aria-hidden="true">
            <rect x="1.5" y="4" width="15" height="10" fill="none" stroke="#a9a9a9" stroke-width="1.4"/>
            <path d="M1.5 4l7.5 6 7.5-6" fill="none" stroke="#a9a9a9" stroke-width="1.4"/>
          </svg>
          <span>quietgoldenhour.com.au</span>
        </li>
        <li class="contact-item">
          <svg class="contact-icon" viewBox="0 0 18 18" aria-hidden="true">
            <path d="M2 7c0-2.5 3.2-4 7-4s7 1.5 7 4l-3 0.6-0.6-2H5.6L5 7.6z" fill="#a9a9a9"/>
            <path d="M4.5 9h9l1.5 6H3z" fill="#a9a9a9"/>
          </svg>
          <span>0418592036</span>
        </li>
      </ul>
    </section>
  </main>
</body>
</html>
```